Tree Pruning Website

We need a website for a tree Arborist, pruning company called Hollow Ridge Groundcare. We look after all types of trees, knock down trees and prune trees. Our target market is from domestic clients to government clients and everything in between.

We would like to see the use of our main colours which are orange and green

We are not looking forward in seeing a template that we have seen before but a unique template. We have designed 5 templates ourselves and we wish for the design community to take our designs to the next level.

We have also designed a template for things that **we are not** looking for (Version 4)

To make it fair for everyone, we are also not giving out any participation payments as we have had. One winner will take all of the payment!!!

I Have attached a image of the designs and a image of a tree.

We are just looking at the PSD file been developed. We have our own team who can slice the image up into a HTML format.

Target Market(s)

Everyone who needs to cut down a tree

Industry/Entity Type

Government

Requirements
Must have
• Logo on front page
A List of our services
jQuery slider on page
Phone Number on every page

```html
<!DOCTYPE html>
<html lang="en">
<head>
<meta charset="utf-8">
<title>Hollow Ridge Groundcare</title>
<link href="https://fonts.googleapis.com/css2?family=PT+Sans:wght@400;700&family=PT+Sans+Narrow:wght@400;700&display=swap" rel="stylesheet">
<style>
:root{
  --green:#4f8a46;
  --green-dark:#2c4f25;
  --green-band:#5a8d4c;
  --orange:#e08a14;
  --text:#7a7a7a;
  --text-dark:#555;
  --panel:#f4f4f4;
  --footer:#3d3d3d;
  --bark:#1c130d;
}
*{box-sizing:border-box;margin:0;padding:0}
html,body{width:1200px;height:1114px;overflow:hidden;background:#fff}
body{position:relative;font-family:"PT Sans",sans-serif;color:var(--text)}
.top-strip{position:absolute;left:0;top:0;width:1200px;height:8px;background:var(--green)}
.hero{position:absolute;left:0;top:8px;width:1200px;height:348px;
  background:radial-gradient(ellipse 48% 80% at 50% 45%,#8fae3c 0%,#5f8a2a 40%,#3e5c20 65%,var(--bark) 100%)}
.site-header{position:absolute;left:171px;top:8px;width:858px;height:75px;background:rgba(245,245,240,.93)}
.brand{position:absolute;left:12px;top:26px;display:flex;align-items:center;gap:8px;
  font-family:"PT Sans",sans-serif;font-weight:700;font-size:17px;color:var(--green)}
.brand-dot{width:16px;height:16px;border-radius:50%;background:var(--orange)}
.main-nav{position:absolute;right:24px;top:29px;display:flex;gap:32px;font-size:13px;letter-spacing:1px;text-transform:uppercase;color:#777}
.main-nav .active{color:var(--orange)}
.headline{position:absolute;left:170px;color:#fff;font-size:28px;letter-spacing:2px;padding:0 11px;height:46px;line-height:46px}
.headline.one{top:152px;background:var(--green)}
.headline.two{top:208px;background:var(--green-dark)}
.callout{position:absolute;left:0;top:356px;width:1200px;height:61px;
  background:linear-gradient(#dedede 0,#dedede 4px,#fafafa 5px,#efefef 100%);
  display:flex;justify-content:center;align-items:center;gap:27px;padding-top:4px;font-size:20px;letter-spacing:1.5px}
.callout .msg{color:#666}
.callout .cta{color:var(--orange)}
.service-band{position:absolute;left:0;top:417px;width:1200px;height:48px;background:var(--green-band)}
.service-btn{position:absolute;top:8px;width:133px;height:32px;background:linear-gradient(#3f6e36,#234a1f);
  border:1px solid #6e9a62;color:#fff;font-family:"PT Sans Narrow",sans-serif;font-size:16px;letter-spacing:1.5px;text-align:center;line-height:30px}
.intro{position:absolute;left:174px;top:483px;width:510px}
.intro h1{font-family:"PT Sans Narrow",sans-serif;font-weight:400;font-size:22px;letter-spacing:1px;color:var(--text-dark);
  padding-bottom:8px;border-bottom:3px solid #ccc;width:507px}
.intro .body{margin-top:20px;font-size:12.3px;line-height:20.6px;letter-spacing:.5px}
.intro .photo{float:left;width:175px;height:112px;margin:0 16px 2px 1px;background:linear-gradient(135deg,#3a5a22,#6d8a3a 50%,#2e4419)}
.intro a{color:var(--green);text-decoration:none}
.checklist{position:absolute;left:174px;top:807px;width:520px;display:grid;grid-template-columns:273px 247px;row-gap:14px;
  list-style:none;font-size:12.5px;letter-spacing:.7px}
.checklist li{display:flex;align-items:center;gap:10px;height:20px}
.checklist svg{width:17px;height:17px;flex:none}
.news{position:absolute;left:736px;top:483px;width:292px;height:522px;background:var(--panel);padding:8px 15px 0 19px}
.news h2{font-family:"PT Sans Narrow",sans-serif;font-weight:400;font-size:17px;letter-spacing:1px;color:var(--green-dark);margin-bottom:10px}
.news-item{border-bottom:1px dotted #aaa;padding-bottom:14px;margin-bottom:12px}
.news-item time{display:block;font-family:"PT Sans Narrow",sans-serif;font-size:11px;color:#666;margin-bottom:9px}
.news-item p{font-size:12.3px;line-height:20.6px;letter-spacing:.5px;color:#666}
.news-item a{display:block;margin-top:8px;font-size:10.5px;color:var(--orange);text-decoration:none;letter-spacing:.5px}
.site-footer{position:absolute;left:0;top:1046px;width:1200px;height:68px;background:var(--footer);
  font-family:"PT Sans Narrow",sans-serif;font-size:10px;letter-spacing:.5px;text-transform:uppercase;color:#aaa}
.footer-nav{position:absolute;left:172px;top:31px;display:flex;gap:29px}
.footer-nav .active,.site-footer .biz{color:var(--green-band)}
.legal{position:absolute;right:182px;top:31px}
</style>
</head>
<body>
<div class="top-strip"></div>
<div class="hero" role="img" aria-label="Photo looking up through a green tree canopy with sun flare"></div>

<header class="site-header">
  <div class="brand"><span class="brand-dot"></span>Hollow Ridge Groundcare</div>
  <nav class="main-nav">
    <span class="active">Home</span><span>About</span><span>Services</span><span>Areas Covered</span><span>News</span><span>Contact</span>
  </nav>
</header>

<div class="headline one">LOREM IPSUM DOLO</div>
<div class="headline two">CONSECTETUR ADIPISCI</div>

<section class="callout">
  <span class="msg">Mauris non ligula in sapien vestibulum iaculis dignissim</span>
  <span class="cta">Get in touch &gt;</span>
</section>

<nav class="service-band">
  <div class="service-btn" style="left:171px">diagnosis</div>
  <div class="service-btn" style="left:317px">diagnosis</div>
  <div class="service-btn" style="left:463px">diagnosis</div>
  <div class="service-btn" style="left:609px">diagnosis</div>
  <div class="service-btn" style="left:753px">diagnosis</div>
  <div class="service-btn" style="left:897px">diagnosis</div>
</nav>

<main class="intro">
  <h1>Sapien vestibulum iaculis ullone sate</h1>
  <div class="body">
    <div class="photo" role="img" aria-label="Tree surgeon pruning branches among leaves"></div>
    Lorem ipsum dolor sit amet, consectetur adipiscing elit. <a href="#">Morbi posuere,</a> sapien at iaculis sodales, ante nisl congue urna, vel vehicula dolor eros a risus. Suspendisse potenti. Maecenas eu metus tortor, eget venenatis nisi. Vivamus semper feugiat posuere. Pellentesque nibh leo, iaculis neclatte enreiqe vel vehicula dolor erosings lat Donec molestie nulla nec risus pharetra eu <a href="#">convallis odio imperdiet</a>. Suspendisse imperdiet mi ac eros eleifend molestie sollicitudin orci fermentum. Ut consectetur mollis sem, et bibendum sem laoreet sed ullam urna neque.<br>
    Imperdiet pellentesque <a href="#">scelerisque</a> sed, iaculis ut diam. Proin consequat, diam a semper vehicula, nisl risus tristique erat, nec elementum orci enim nec massa. Morbi orci lectus, fermentum in elementum in, ornare id lectus..
  </div>
</main>

<ul class="checklist">
  <li><svg viewBox="0 0 20 20"><circle cx="10" cy="10" r="10" fill="#e08a14"/><path d="M8 6l6 4-6 4z" fill="#fff"/></svg>Proin consequat, diam a semper</li>
  <li><svg viewBox="0 0 20 20"><circle cx="10" cy="10" r="10" fill="#4f8a46"/><path d="M8 6l6 4-6 4z" fill="#fff"/></svg>Proin consequat, diam a semper</li>
  <li><svg viewBox="0 0 20 20"><circle cx="10" cy="10" r="10" fill="#4f8a46"/><path d="M8 6l6 4-6 4z" fill="#fff"/></svg>Vehicula nisl risus tristique erat</li>
  <li><svg viewBox="0 0 20 20"><circle cx="10" cy="10" r="10" fill="#e08a14"/><path d="M8 6l6 4-6 4z" fill="#fff"/></svg>Vehicula nisl risus tristique erat</li>
  <li><svg viewBox="0 0 20 20"><circle cx="10" cy="10" r="10" fill="#e08a14"/><path d="M8 6l6 4-6 4z" fill="#fff"/></svg>Nec elementum orci enim nec</li>
  <li><svg viewBox="0 0 20 20"><circle cx="10" cy="10" r="10" fill="#4f8a46"/><path d="M8 6l6 4-6 4z" fill="#fff"/></svg>Nec elementum orci enim nec</li>
  <li><svg viewBox="0 0 20 20"><circle cx="10" cy="10" r="10" fill="#4f8a46"/><path d="M8 6l6 4-6 4z" fill="#fff"/></svg>Ellen rangering sorttery minserte</li>
  <li><svg viewBox="0 0 20 20"><circle cx="10" cy="10" r="10" fill="#e08a14"/><path d="M8 6l6 4-6 4z" fill="#fff"/></svg>Ellen rangering sorttery minserte</li>
</ul>

<aside class="news">
  <h2>Latest News</h2>
  <article class="news-item">
    <time>12th January 2013</time>
    <p>Maecenas eu metus tortor, eget venenatis nisi. Vivamus semper feugiat posuere. Pellentesque nibh leo, iaculis neclatte enreiqe vel vehicula dolor erosings lat</p>
    <a href="#">read more</a>
  </article>
  <article class="news-item">
    <time>12th September 2012</time>
    <p>Maecenas eu metus tortor, eget venenatis nisi. Vivamus semper feugiat posuere. Pellentesque nibh leo, iaculis neclatte enreiqe vel vehicula dolor erosings lat</p>
    <a href="#">read more</a>
  </article>
  <article class="news-item">
    <time>12th September 2012</time>
    <p>Maecenas eu metus tortor, eget venenatis nisi. Vivamus semper feugiat posuere. Pellentesque nibh leo, iaculis neclatte enreiqe vel vehicula dolor erosings lat</p>
    <a href="#">read more</a>
  </article>
</aside>

<footer class="site-footer">
  <nav class="footer-nav"><span class="active">Home</span><span>About</span><span>News</span><span>Services</span><span>Contact</span></nav>
  <div class="legal">Copyright © 2013 &nbsp;<span class="biz">Business Name</span> | All rhights reserved</div>
</footer>
</body>
</html>
```